Building Company Business Card Design

Need a design for a business card:
It needs to have: Name, Phone, Facebook link, Website, email
i would also like a list of works we undertake:
-New Homes
-Extensions, Renovations & Bathrooms
-Decking, Carports, Sheds (Residential and Industrial)
-Carpentry
-Fences, Patios & Pergolas

Name, Phone, Facebook link, Website, email + details of services provided listed in description

```html
<!DOCTYPE html>
<html lang="en">
<head>
<meta charset="utf-8">
<title>Ridgeline Homes – Business Card</title>
<link href="https://fonts.googleapis.com/css2?family=Michroma&family=Montserrat:wght@600;700&display=swap" rel="stylesheet">
<style>
  :root{
    --stage:#3a3a3a;
    --card-dark:#0d0d0d;
    --card-light:#f7f7f7;
    --green:#2eac49;
    --green-soft:#dcefe0;
    --grey:#8a8a8a;
    --grey-mid:#7b7b7b;
    --grey-pale:#ececec;
    --ink:#1d1d1d;
    --white:#ffffff;
  }
  *{margin:0;padding:0;box-sizing:border-box}
  html,body{width:1200px;height:900px;overflow:hidden;background:var(--stage)}
  .canvas{position:relative;width:1200px;height:900px}
  .card{position:absolute;left:250px;width:700px;height:400px;border-radius:26px;overflow:hidden}
  .card--front{top:40px;background:var(--card-dark)}
  .card--back{top:460px;background:var(--card-light)}

  .feature-graphic{position:absolute;left:330px;top:0;width:370px;height:400px;
    background:linear-gradient(150deg,var(--green) 0%,var(--green) 42%,var(--grey-mid) 58%,var(--grey-mid) 100%);
    clip-path:polygon(42% 0,100% 0,100% 100%,0 100%)}

  .brand-title{position:absolute;left:52px;top:62px;font-family:"Michroma",sans-serif;color:var(--white)}
  .brand-title__name{font-size:27px;letter-spacing:1px;line-height:1}
  .brand-title__sub{font-size:11.5px;color:var(--grey);letter-spacing:1.4px;margin-top:6px}
  .brand-title__rule{width:330px;height:2px;background:var(--green);margin-top:10px}

  .services{position:absolute;left:52px;top:146px;list-style:none;font-family:"Montserrat",sans-serif;font-weight:700;font-size:13.5px;color:var(--white);text-transform:uppercase;line-height:1.05}
  .services li{position:relative;padding-left:20px;margin-bottom:13px}
  .services li::before{content:"";position:absolute;left:2px;top:5px;width:5px;height:5px;border-radius:50%;background:var(--green)}

  .back-graphic{position:absolute;left:380px;top:0;width:320px;height:400px;
    background:linear-gradient(160deg,var(--green-soft) 0%,var(--grey-pale) 100%);
    clip-path:polygon(40% 0,100% 0,100% 100%,0 100%);opacity:.8}

  .wordmark{position:absolute;left:40px;top:176px;display:flex;align-items:center;gap:12px;font-family:"Michroma",sans-serif;color:var(--ink)}
  .wordmark__mark{width:18px;height:18px;background:var(--green);flex:none}
  .wordmark__name{font-size:19px;line-height:1.15;letter-spacing:.3px;white-space:nowrap}
  .wordmark__name span{display:block;font-size:8.8px;letter-spacing:1.1px}

  .divider{position:absolute;left:372px;top:70px;width:1px;height:260px;background:#9a9a9a}

  .contact{position:absolute;left:408px;top:92px;font-family:"Montserrat",sans-serif}
  .contact__name{font-size:20px;font-weight:700;color:var(--ink);letter-spacing:.5px}
  .contact__role{font-size:13px;font-weight:700;color:var(--grey);letter-spacing:.5px;margin-top:2px}
  .contact__list{list-style:none;margin-top:26px}
  .contact__list li{display:flex;align-items:center;gap:10px;font-size:14.5px;font-weight:600;color:var(--ink);margin-bottom:5px}
  .contact__list li.gap{margin-top:16px}
  .contact__list svg{width:15px;height:15px;flex:none}
</style>
</head>
<body>
<main class="canvas">

  <section class="card card--front">
    <div class="feature-graphic" role="img" aria-label="Large green and grey brand graphic"></div>
    <header class="brand-title">
      <div class="brand-title__name">RIDGELINE HOMES</div>
      <div class="brand-title__sub">AND DEVELOPMENTS PTY LTD</div>
      <div class="brand-title__rule"></div>
    </header>
    <ul class="services">
      <li>New Homes</li>
      <li>Extensions,<br>Renovations<br>&amp; Bathrooms</li>
      <li>Decking, Carports,<br>Sheds (Residential<br>&amp; Industrial)</li>
      <li>Carpentry</li>
      <li>Fences, Patios<br>&amp; Pergolas</li>
    </ul>
  </section>

  <section class="card card--back">
    <div class="back-graphic" role="img" aria-label="Faint pale brand graphic"></div>
    <div class="wordmark">
      <div class="wordmark__mark"></div>
      <div class="wordmark__name">RIDGELINE HOMES<span>AND DEVELOPMENTS PTY LTD</span></div>
    </div>
    <div class="divider"></div>
    <div class="contact">
      <div class="contact__name">DANIEL HARROW</div>
      <div class="contact__role">MANAGING DIRECTOR</div>
      <ul class="contact__list">
        <li><svg viewBox="0 0 16 16"><rect x="4" y="1" width="8" height="14" rx="1.5" fill="none" stroke="var(--green)" stroke-width="1.8"/><circle cx="8" cy="12.3" r="0.9" fill="var(--green)"/></svg>555 0142 7788</li>
        <li><svg viewBox="0 0 16 16"><rect x="1" y="3" width="14" height="10" rx="1" fill="var(--green)"/><path d="M1.5 4 8 9l6.5-5" fill="none" stroke="var(--white)" stroke-width="1.3"/></svg>d.harrow@ridgelinehomes.com</li>
        <li class="gap"><svg viewBox="0 0 16 16"><g fill="none" stroke="var(--green)" stroke-width="1.4"><circle cx="8" cy="8" r="6.5"/><ellipse cx="8" cy="8" rx="3" ry="6.5"/><path d="M1.5 8h13M2.5 4.5h11M2.5 11.5h11"/></g></svg>www.ridgelinehomes.com</li>
        <li><svg viewBox="0 0 16 16"><circle cx="8" cy="8" r="6" fill="var(--green)"/></svg>ridgelinehomes</li>
      </ul>
    </div>
  </section>

</main>
</body>
</html>
```